Dana's Pup Suds & Snip

I have a mobile dog grooming business and I need a design. I would like a scruffy dirty dog as a before dog. Then a clean short hair neatly groomed dog as the after been cleaned and groom by my service. Cartoon images would be good.
My services are bathing, drying, cleaning ears, clipping nails, clip and style hair and deodorising. The mobile van is white and my mobile number is 0461302857.
No dog in bath/tub designs please as they are too common.

Target Market(s)

Clients who wish their dogs to be clean and clipped, ready for the summer heat and Christmas where friends and family visit. They want their dog smelling nice and looking good.

Industry/Entity Type

Graphic Design

Contact Information for Business Card

DANA'S PUP SUDS & SNIP Mobile Grooming
Bath, Trim Nails, Clean Ears, Style Clip, Blow Dry,
Cologne. Call Us On: 0461302857

Font styles to use
Script

Colors
85cae6
34a6d7
0393ce
ec1f27

Requirements
Must have
• A Logo with a picture of 2 dogs.. One dirty dog, scruffy long hair, messy, neglected
• 2nd Dog, Clean, Hair neat Looking Sharp and well
• looked after.
• A comparison of two dogs the before and after shots of the same dog. Before it was groomed and after it was groomed. Cartoon form.
Nice to have
• The colour of my Van is White with a light blue stripe at the bottom. I would like colours to suit my trailer eg Grey's, Bubbles, or water drops. Red & Black writing.
• As I need business cards and vinyl sticker logo to put on my trailer.
Should not have
• No dogs in baths or tubs as they are too common in the Mobile Grooming Industry.
• Needs to be unique. .

```html
<!DOCTYPE html>
<html lang="en">
<head>
<meta charset="utf-8">
<title>Dana's Pup Suds &amp; Snip – Business Card</title>
<link rel="stylesheet" href="https://fonts.googleapis.com/css2?family=Great+Vibes&family=Montserrat:wght@400;800&family=Questrial&display=swap">
<style>
  :root {
    --sky: #85cae6;
    --ocean: #34a6d7;
    --deep-blue: #0393ce;
    --red: #ec1f27;
    --ink: #222428;
    --paper: #ffffff;
    --backdrop: #e9ecef;
    --muted: #5a5f8a;
    --dog-dark: #141414;
    --dog-mid: #3a3a3a;
  }
  * { box-sizing: border-box; margin: 0; padding: 0; }
  html, body {
    width: 1200px;
    height: 855px;
    overflow: hidden;
    background: var(--backdrop);
  }
  .canvas {
    position: relative;
    width: 1200px;
    height: 855px;
  }
  .business-card {
    position: absolute;
    left: 190px;
    top: 50px;
    width: 820px;
    height: 470px;
    background: var(--paper);
    border-radius: 28px;
    overflow: hidden;
    box-shadow: 0 14px 34px rgba(0, 0, 0, 0.18);
  }
  .card-band {
    position: absolute;
    inset: 0;
    width: 820px;
    height: 470px;
  }
  .dog-art {
    background: linear-gradient(160deg, var(--dog-mid), var(--dog-dark));
    border-radius: 14px;
  }
  .card-dog {
    position: absolute;
    top: 22px;
    width: 130px;
    height: 108px;
  }
  .card-dog--before { left: 34px; }
  .card-dog--after { right: 34px; }
  .card-logo {
    position: absolute;
    top: 50px;
    left: 180px;
    width: 460px;
    text-align: center;
    font-family: "Great Vibes", cursive;
    font-weight: 400;
    font-size: 48px;
    line-height: 1;
    color: var(--deep-blue);
    white-space: nowrap;
  }
  .band-copy {
    position: absolute;
    left: 60px;
    top: 182px;
    width: 720px;
    text-align: center;
    color: var(--paper);
    transform: rotate(3.2deg);
  }
  .band-title {
    font-family: "Great Vibes", cursive;
    font-size: 52px;
    line-height: 1.05;
  }
  .band-services {
    margin-top: 6px;
    font-family: "Questrial", sans-serif;
    font-size: 23px;
    line-height: 1.3;
    word-spacing: 6px;
  }
  .card-footer {
    position: absolute;
    left: 70px;
    top: 388px;
    transform: rotate(3.2deg);
    transform-origin: left center;
  }
  .tagline {
    font-family: "Montserrat", sans-serif;
    font-weight: 800;
    font-size: 22px;
    letter-spacing: 0.5px;
    color: var(--ink);
  }
  .phone {
    display: flex;
    align-items: center;
    gap: 8px;
    margin-top: 6px;
    font-family: "Montserrat", sans-serif;
    font-weight: 400;
    font-size: 24px;
    color: var(--red);
  }
  .phone-icon { width: 22px; height: 22px; }
  .abn {
    position: absolute;
    right: 34px;
    bottom: 22px;
    font-family: "Montserrat", sans-serif;
    font-size: 13px;
    color: var(--muted);
    letter-spacing: 0.5px;
  }
  .logo-lockup {
    position: absolute;
    left: 0;
    top: 600px;
    width: 1200px;
    display: flex;
    align-items: center;
    justify-content: center;
    gap: 28px;
  }
  .lockup-dog {
    width: 160px;
    height: 150px;
    flex: none;
  }
  .lockup-name {
    font-family: "Great Vibes", cursive;
    font-weight: 400;
    font-size: 76px;
    line-height: 1.2;
    color: var(--deep-blue);
    white-space: nowrap;
  }
</style>
</head>
<body>
<main class="canvas">
  <section class="business-card">
    <svg class="card-band" viewBox="0 0 820 470" aria-hidden="true">
      <defs>
        <linearGradient id="bandFill" x1="0" y1="0" x2="1" y2="0.3">
          <stop offset="0" stop-color="var(--sky)"/>
          <stop offset="0.45" stop-color="var(--ocean)"/>
          <stop offset="1" stop-color="var(--deep-blue)"/>
        </linearGradient>
      </defs>
      <path d="M0,150 Q410,158 820,218 L820,392 Q410,336 0,322 Z" fill="url(#bandFill)"/>
      <path d="M0,150 Q410,158 820,218" fill="none" stroke="var(--red)" stroke-width="3"/>
      <path d="M0,322 Q410,336 820,392" fill="none" stroke="var(--red)" stroke-width="3"/>
      <g fill="rgba(255,255,255,0.18)" stroke="rgba(255,255,255,0.6)" stroke-width="1.2">
        <circle cx="140" cy="200" r="22"/>
        <circle cx="178" cy="180" r="9"/>
        <circle cx="700" cy="330" r="26"/>
        <circle cx="748" cy="300" r="11"/>
        <circle cx="650" cy="360" r="8"/>
      </g>
    </svg>

    <div class="dog-art card-dog card-dog--before" role="img" aria-label="Black silhouette of a scruffy, long-haired dog before grooming"></div>
    <h1 class="card-logo">Dana's Pup Suds &amp; Snip</h1>
    <div class="dog-art card-dog card-dog--after" role="img" aria-label="Black silhouette of a neatly clipped dog with a red bow after grooming"></div>

    <div class="band-copy">
      <p class="band-title">Mobile Dog Grooming Service</p>
      <p class="band-services">Bathing, Clipping, Styling, Blow Drying, Clipping nails,<br>Cleaning ears, Flea Treatments, and Deodorising</p>
    </div>

    <div class="card-footer">
      <p class="tagline">GROOMING DOGS FROM HEAD TO TAIL</p>
      <p class="phone">
        <svg class="phone-icon" viewBox="0 0 22 22" aria-hidden="true">
          <circle cx="11" cy="11" r="11" fill="var(--red)"/>
          <rect x="7" y="5" width="8" height="12" rx="1.5" fill="none" stroke="#fff" stroke-width="1.6"/>
          <circle cx="11" cy="14.5" r="0.9" fill="#fff"/>
        </svg>
        0461302857
      </p>
    </div>

    <p class="abn">ABN: 47 215 608 942</p>
  </section>

  <div class="logo-lockup">
    <div class="dog-art lockup-dog" role="img" aria-label="Scruffy long-haired dog silhouette, the before look"></div>
    <p class="lockup-name">Dana's Pup Suds &amp; Snip</p>
    <div class="dog-art lockup-dog" role="img" aria-label="Neatly groomed dog silhouette with a red bow, the after look"></div>
  </div>
</main>
</body>
</html>
```